Bright Meadow Counseling Business Card design with a visually interesting use of Space

I need business cards that are luxurious and give a peaceful, calm vibe. I also had some letterhead designed, and i like the look of it also, it's attached with the logo design for reference/ ideas but feel free to be creative.

Target Market(s)

High end luxurious client who needs counseling

Industry/Entity Type

Marriage and Family Therapy

Contact Information for Business Card

Mira Kowalczyk MS LMFT/ or Toby Hallett address 4150 Larkin Suite 600

Font styles to use
Sans Serif

Colors
0054AA
0677BA
7BADD7
CADEEF
E8F1F8
0094D4
00A9DD
6FCCEA
C7EBF8
E9F6FB
A7469A
B969AE
D3A5CF
EDDBEB
F8F0F9
6B429C
8869AF
B7A5CE
E3DAEB
F3F0F8

Requirements
Must have
• Logo and color scheme but be simple modern and luxurious
Nice to have
• I'd like to incorporate some elelmets from the logo and letterhead into a simple modern card

```html
<!DOCTYPE html>
<html lang="en">
<head>
<meta charset="utf-8">
<title>Bright Meadow Counseling — Business Card</title>
<link rel="stylesheet" href="https://fonts.googleapis.com/css2?family=Jost:wght@300&family=Source+Sans+3:wght@400;600&display=swap">
<style>
  :root {
    --canvas: #e4e5e6;
    --card-dark: #262626;
    --card-light: #f4f4f4;
    --ink: #1d1d1d;
    --white: #ffffff;
    --purple: #6b2f92;
    --magenta: #922a84;
    --blue: #1a70b6;
    --teal: #17a39a;
    --bubble-purple: #8869af;
    --bubble-blue: #0677ba;
    --bubble-teal: #3fb8a8;
    --bubble-pink: #a7469a;
  }
  * { margin: 0; padding: 0; box-sizing: border-box; }
  html, body { width: 1200px; height: 960px; overflow: hidden; }
  body {
    position: relative;
    background: var(--canvas);
    font-family: "Source Sans 3", Arial, sans-serif;
    color: var(--ink);
  }
  .card {
    position: absolute;
    left: 299px;
    width: 605px;
    height: 346px;
    overflow: hidden;
  }

  /* Front */
  .card-front { top: 114px; background: var(--card-dark); color: var(--white); }
  .wordmark { position: absolute; text-align: right; font-family: "Jost", Arial, sans-serif; font-weight: 300; line-height: 1; }
  .card-front .wordmark { right: 207px; top: 148px; }
  .wordmark-name { display: block; }
  .wordmark-sub { display: block; letter-spacing: 0.08em; }
  .card-front .wordmark-name { font-size: 48px; }
  .card-front .wordmark-sub { font-size: 25px; margin-top: 6px; }
  .front-url {
    position: absolute; left: 0; right: 0; top: 286px;
    text-align: center; font-size: 18px; letter-spacing: 0.06em;
  }
  .color-bar { position: absolute; left: 0; right: 0; bottom: 0; height: 14px; display: flex; }
  .color-bar span { flex: 1; }
  .bar-purple { background: var(--purple); }
  .bar-magenta { background: var(--magenta); }
  .bar-blue { background: var(--blue); }
  .bar-teal { background: var(--teal); }

  /* Back */
  .card-back { top: 514px; background: var(--card-light); }
  .bubble-field { position: absolute; left: 0; top: 0; width: 370px; height: 346px; }
  .card-back .wordmark { right: 39px; top: 40px; color: var(--ink); }
  .card-back .wordmark-name { font-size: 35px; }
  .card-back .wordmark-sub { font-size: 19px; margin-top: 3px; }
  .holder { position: absolute; left: 53px; top: 172px; color: var(--white); }
  .holder-name { font-size: 20px; font-weight: 600; line-height: 24px; }
  .holder-role { font-size: 15px; line-height: 20px; }
  .address { position: absolute; right: 39px; top: 174px; text-align: right; font-size: 16px; line-height: 20px; }
  .contacts { position: absolute; right: 39px; top: 232px; list-style: none; text-align: right; font-size: 16px; line-height: 20.3px; }
  .contacts li { display: flex; justify-content: flex-end; align-items: center; gap: 4px; }
  .contacts svg { width: 14px; height: 14px; }
</style>
</head>
<body>
  <section class="card card-front">
    <div class="wordmark">
      <span class="wordmark-name">Bright Meadow</span>
      <span class="wordmark-sub">Counseling</span>
    </div>
    <p class="front-url">www.BrightMeadow.com</p>
    <div class="color-bar">
      <span class="bar-purple"></span><span class="bar-magenta"></span><span class="bar-blue"></span><span class="bar-teal"></span>
    </div>
  </section>

  <section class="card card-back">
    <svg class="bubble-field" viewBox="0 0 370 346" role="img" aria-label="Large overlapping translucent circles in purple, blue, teal and magenta">
      <defs>
        <radialGradient id="bubbleGlow" cx="0.4" cy="0.5" r="0.6">
          <stop offset="0" stop-color="var(--bubble-purple)"/>
          <stop offset="0.45" stop-color="var(--bubble-blue)" stop-opacity="0.85"/>
          <stop offset="0.75" stop-color="var(--bubble-pink)" stop-opacity="0.55"/>
          <stop offset="1" stop-color="var(--bubble-teal)" stop-opacity="0"/>
        </radialGradient>
      </defs>
      <rect width="370" height="346" fill="url(#bubbleGlow)"/>
    </svg>

    <div class="wordmark">
      <span class="wordmark-name">Bright Meadow</span>
      <span class="wordmark-sub">Counseling</span>
    </div>

    <div class="holder">
      <p class="holder-name">Daniel Marsh</p>
      <p class="holder-role">President</p>
    </div>

    <address class="address" style="font-style:normal">
      2214 Willow Crest Road<br>Fairview, Oregon 97024
    </address>

    <ul class="contacts">
      <li>555-214-7730
        <svg viewBox="0 0 14 14" aria-hidden="true"><path d="M3 1.5l2 2.6-1.2 1.3a7 7 0 0 0 4.8 4.8l1.3-1.2 2.6 2-1.3 1.8C6.5 12.8 1.2 7.5 1.2 2.8z" fill="var(--purple)"/></svg>
      </li>
      <li>555-214-7731
        <svg viewBox="0 0 14 14" aria-hidden="true"><rect x="3.5" y="1.5" width="7" height="4" fill="none" stroke="var(--magenta)" stroke-width="1.3"/><rect x="1" y="5" width="12" height="6" rx="1" fill="var(--magenta)"/><rect x="3.5" y="9" width="7" height="3.5" fill="var(--white)" stroke="var(--magenta)"/></svg>
      </li>
      <li>hello@brightmeadow.com
        <svg viewBox="0 0 14 14" aria-hidden="true"><rect x="1" y="2.5" width="12" height="9" fill="var(--blue)"/><path d="M1.5 3l5.5 4.5L12.5 3" fill="none" stroke="var(--white)" stroke-width="1.1"/></svg>
      </li>
      <li>www.brightmeadow.com
        <svg viewBox="0 0 14 14" aria-hidden="true"><g fill="none" stroke="var(--teal)" stroke-width="1.1"><circle cx="7" cy="7" r="5.8"/><ellipse cx="7" cy="7" rx="2.6" ry="5.8"/><path d="M1.2 7h11.6M2 4h10M2 10h10"/></g></svg>
      </li>
    </ul>
  </section>
</body>
</html>
```